Brightwell Pixel - Design & Marketing Website Re-branding

UPDATE:
We are working on finalizing our color palette but are hoping that the designers will guide us to the right choice of colors by looking at our color inspiration file that we just uploaded and lead us in the right direction.

-----

I am exploring new design inspiration for a re-branding of my website. My current website is old and outdated and I lack the time to design it myself in addition to the fact that I am my own worst client.

I do website design, development and marketing as well as some SEO consulting and business development for small to mid-size companies in a range of industries.

https://brightwellpixel-example.com

I like clean modern designs without cartoon images. The brands I'm going after are looking for a professional look and feel. I need something that shows my many years of being in business that is very professional.

I prefer minimal use of color. Mostly black and white with maybe one or two other colors. I am open to the suggestions by the designer.

Target Market(s)

Small to mid-size companies

Industry/Entity Type

Website Design, SEO and Markeitng

Number of Pages Required

4 page

Font styles to use
Sans Serif

Requirements
Must have
• Must be clean, modern and professional - I am not a huge fan of a lot of color and I'm open to new color suggestions by the designer
Nice to have
• A good balance of whitespace to content and graphics
Should not have
• Please no people illustrations

```html
<!DOCTYPE html>
<html lang="en">
<head>
<meta charset="utf-8">
<title>Brightwell Pixel — Every business has a story</title>
<link href="https://fonts.googleapis.com/css2?family=Poppins:wght@500;600;700&family=Roboto:wght@400;500;700&display=swap" rel="stylesheet">
<style>
:root{
  --pink:#c07aa9;
  --pink-soft:#f3e6ef;
  --ink:#1f1f1f;
  --grey:#5a5a5a;
  --muted:#6f6f6f;
  --dark:#2a2a2a;
  --light:#f5f5f5;
  --line:#e6e6e6;
  --white:#ffffff;
}
*{box-sizing:border-box;margin:0;padding:0}
html,body{width:1200px;height:3827px;overflow:hidden;background:var(--white)}
body{font-family:"Roboto",Arial,sans-serif;color:var(--ink);position:relative}
section,footer,header{position:relative;width:1200px}
.abs{position:absolute}
.heading{font-family:"Poppins",Arial,sans-serif;font-weight:600}
.dot{color:var(--pink)}
.btn{position:absolute;background:var(--pink);color:var(--white);border-radius:30px;font-weight:500;font-size:15px;display:flex;align-items:center;justify-content:center;gap:8px;text-transform:uppercase}
.btn .arrow{width:14px;height:14px;border-radius:50%;background:var(--white);display:inline-flex;align-items:center;justify-content:center}
.btn .arrow::after{content:"";border-left:5px solid var(--pink);border-top:3.5px solid transparent;border-bottom:3.5px solid transparent;margin-left:2px}

/* hero */
.hero{height:678px}
.network{left:180px;top:30px;width:1020px;height:648px;background:linear-gradient(200deg,#d9d9d9 0%,#f2f2f2 45%,#fff 70%);clip-path:polygon(100% 0,100% 100%,0 100%,40% 72%,60% 40%,85% 10%)}
.logo{font-family:"Poppins",Arial,sans-serif;font-weight:500;font-size:30px;letter-spacing:-0.5px;color:var(--ink)}
.nav{left:440px;top:40px;display:flex;gap:20px;font-size:14px;font-weight:500}
.nav .active{color:var(--pink)}
.eyebrow{left:143px;top:209px;font-size:13px;color:var(--pink);letter-spacing:.3px}
.hero h1{left:143px;top:226px;font-size:43px;line-height:54px}
.hero h1 .soft{color:#555}
.hero .lead{left:143px;top:357px;font-size:15px}

/* what we do */
.services{height:512px;background:var(--dark)}
.section-title{position:absolute;left:0;width:100%;text-align:center;font-size:36px}
.services .section-title{top:66px;color:var(--white)}
.services .section-title .faint{color:#b8b8b8}
.service-card{position:absolute;top:152px;width:279px;height:281px;background:var(--white);border-radius:12px;padding:30px 23px}
.service-card svg{display:block;margin-bottom:22px}
.service-card h3{font-size:17px;font-weight:500;margin-bottom:14px}
.service-card p{font-size:13px;line-height:22px;color:var(--muted);margin-bottom:14px}
.service-card a{font-size:13px;color:var(--pink);text-decoration:none;font-weight:500}

/* create */
.create{height:715px}
.create h2{left:143px;top:158px;font-size:38px;line-height:47px}
.create .copy{left:143px;top:276px;width:360px;font-size:13px;line-height:22px;color:var(--grey)}
.create .copy p{margin-bottom:12px}
.backdrop{left:760px;top:155px;width:400px;height:470px;border-radius:50%;background:#f4f4f4}
.backbar{left:1090px;top:0;width:110px;height:520px;background:#f4f4f4}
.feature{position:absolute;width:229px;height:241px;background:var(--white);box-shadow:0 6px 24px rgba(0,0,0,.08);padding:30px 22px}
.feature .icon{width:63px;height:63px;border-radius:12px;background:var(--pink-soft);display:flex;align-items:center;justify-content:center;margin-bottom:22px}
.feature h3{font-size:17px;font-weight:500;margin-bottom:12px}
.feature p{font-size:12.5px;line-height:20px;color:var(--muted);text-align:justify}
.pink-disc{left:1090px;top:527px;width:105px;height:105px;border-radius:50%;background:var(--pink)}

/* explore */
.explore{height:378px;background:var(--light)}
.explore .section-title{top:48px}
.tile{position:absolute;top:129px;width:212px}
.tile .photo{height:156px;border-radius:10px}
.tile span{display:block;text-align:center;margin-top:20px;font-size:17px;font-weight:500}

/* testimonials */
.reviews{height:432px}
.reviews .section-title{top:54px}
.review{position:absolute;top:137px;width:294px;height:202px;background:var(--white);border-radius:8px;box-shadow:0 4px 18px rgba(0,0,0,.08);border-bottom:3px solid var(--pink);padding:22px 24px}
.stars{color:#f0b400;font-size:14px;letter-spacing:2px}
.review p{margin-top:10px;font-size:12px;line-height:21px;color:var(--muted);text-align:justify}
.person{display:flex;align-items:center;gap:12px;margin-top:18px}
.avatar{width:40px;height:40px;border-radius:50%;background:linear-gradient(135deg,#9b7b6b,#cfb7a6)}
.person b{display:block;font-size:14px;font-weight:500}
.person small{font-size:11px;color:var(--muted)}

/* partners */
.partners{height:261px;background:#f3f3f3}
.partners .section-title{top:44px}
.partner{position:absolute;top:120px;width:157px;height:83px;background:var(--white);border-radius:6px;box-shadow:0 3px 12px rgba(0,0,0,.07);display:flex;align-items:center;justify-content:center;font-family:"Poppins",Arial,sans-serif;font-weight:600;font-size:17px;color:#444;gap:8px}
.partner i{width:14px;height:14px;border-radius:50%;background:#bbb;display:inline-block}
.pager{position:absolute;top:146px;width:30px;height:30px;border-radius:50%;background:var(--white);box-shadow:0 2px 8px rgba(0,0,0,.15);display:flex;align-items:center;justify-content:center}

/* contact */
.contact{height:541px;background:var(--dark);overflow:hidden}
.contact .section-title{top:64px;color:var(--white)}
.contact .section-title .faint{color:#b8b8b8}
.ring{left:-130px;top:170px;width:520px;height:520px;border-radius:50%;border:90px solid #3a3a3a}
.field{position:absolute;width:291px;height:40px;background:var(--white);border-radius:2px;font-size:12px;color:#555;padding:12px 12px}
.field.select::after{content:"";position:absolute;right:14px;top:17px;border-top:6px solid #333;border-left:5px solid transparent;border-right:5px solid transparent}
.field.message{width:913px;height:80px}

/* footer */
.site-footer{height:310px}
.social{position:absolute;top:175px;width:34px;height:34px;border-radius:50%;border:1px solid #cfcfcf;display:flex;align-items:center;justify-content:center}
.social i{width:10px;height:10px;border-radius:50%;background:#555}
.divider{position:absolute;top:57px;width:3px;height:42px;background:var(--pink)}
.col-title{position:absolute;top:58px;font-size:14px;font-weight:700;letter-spacing:.4px}
.links{position:absolute;left:538px;top:95px;font-size:13px;line-height:21px;color:#555;list-style:none}
.info{position:absolute;left:810px;font-size:14px;line-height:22px;display:flex;gap:12px}
.copyright{position:absolute;left:143px;top:275px;font-size:12px;color:#555}
.legal{position:absolute;right:144px;top:275px;font-size:12px;color:#555;display:flex;gap:14px}
</style>
</head>
<body>

<header class="hero">
  <div class="abs network" role="img" aria-label="Decorative network of connected dots and lines rising to the right"></div>
  <div class="abs logo" style="left:143px;top:24px">brightwellpixel<span class="dot">.</span></div>
  <nav class="abs nav">
    <span class="active">• Home</span><span>Our Services</span><span>Inspire</span><span>About</span><span>Collaborate</span><span>Connect</span>
  </nav>
  <div class="btn" style="left:910px;top:30px;width:146px;height:42px;text-transform:none;font-size:14px">Get Started</div>
  <div class="abs eyebrow">BRIGHTWELL PIXEL &nbsp;… &nbsp;WELCOME</div>
  <h1 class="abs heading">Every business has a story<span class="dot">.</span><br><span class="soft">We help you tell it<span class="dot">.</span></span></h1>
  <p class="abs lead">Compelling website experiences that elevate your business.</p>
  <div class="btn" style="left:143px;top:418px;width:163px;height:47px">Let’s Chat <span class="arrow"></span></div>
</header>

<section class="services">
  <h2 class="section-title heading"><span class="faint">What</span> We Do</h2>
  <div class="service-card" style="left:145px">
    <svg width="60" height="62" viewBox="0 0 60 62" fill="none" stroke="#c07aa9" stroke-width="1.6"><rect x="4" y="10" width="50" height="34" rx="2"/><line x1="4" y1="38" x2="54" y2="38"/><path d="M22 44v10h14V44M16 56h26"/><rect x="12" y="2" width="16" height="14"/><line x1="14" y1="22" x2="46" y2="22"/><line x1="14" y1="28" x2="40" y2="28"/></svg>
    <h3>Websites Simplified</h3>
    <p>A complete end-to-end website subscription solution that propels your business forward.</p>
    <a>Complete Website Solution »</a>
  </div>
  <div class="service-card" style="left:461px">
    <svg width="60" height="62" viewBox="0 0 60 62" fill="none" stroke="#c07aa9" stroke-width="1.6"><rect x="4" y="4" width="52" height="52" rx="3"/><line x1="4" y1="14" x2="56" y2="14"/><circle cx="32" cy="36" r="10"/><circle cx="32" cy="36" r="4"/><circle cx="10" cy="9" r="1.5"/><circle cx="16" cy="9" r="1.5"/></svg>
    <h3>Custom Website Design</h3>
    <p>A complete end-to-end website subscription solution that propels your business forward.</p>
    <a>Complete Website Solution »</a>
  </div>
  <div class="service-card" style="left:777px">
    <svg width="64" height="62" viewBox="0 0 64 62" fill="none" stroke="#c07aa9" stroke-width="1.6"><rect x="2" y="2" width="44" height="56" rx="2"/><line x1="2" y1="12" x2="46" y2="12"/><circle cx="12" cy="24" r="6"/><line x1="22" y1="22" x2="40" y2="22"/><rect x="8" y="36" width="32" height="14"/><rect x="46" y="24" width="14" height="20" rx="2"/></svg>
    <h3>Websites Simplified</h3>
    <p>A complete end-to-end website subscription solution that propels your business forward.</p>
    <a>Complete Website Solution »</a>
  </div>
</section>

<section class="create">
  <div class="abs backdrop"></div>
  <div class="abs backbar"></div>
  <h2 class="abs heading">We create websites<br>that inspire</h2>
  <div class="abs copy">
    <p>We are a collaborative team of word nerds, choreographers of shapes &amp; ideas, ambassadors of data, content warriors and inspirational conversationalists ready to help you no matter where you are in your journey.</p>
    <p>We have a deep understanding of what it takes to grow a business and we collaborate with you every step of the way from strategy to implementation and beyond.</p>
  </div>
  <div class="btn" style="left:143px;top:476px;width:178px;height:46px">Learn More <span class="arrow"></span></div>
  <div class="feature" style="left:827px;top:92px">
    <div class="icon"><svg width="34" height="34" viewBox="0 0 34 34" fill="none" stroke="#c07aa9" stroke-width="1.5"><circle cx="17" cy="17" r="12"/><ellipse cx="17" cy="17" rx="5" ry="12"/><line x1="5" y1="17" x2="29" y2="17"/><line x1="7" y1="11" x2="27" y2="11"/><line x1="7" y1="23" x2="27" y2="23"/></svg></div>
    <h3>Connection</h3>
    <p>We have carefully crafted each step in our process for successful outcomes.</p>
  </div>
  <div class="feature" style="left:573px;top:224px">
    <div class="icon"><svg width="34" height="34" viewBox="0 0 34 34" fill="none" stroke="#c07aa9" stroke-width="1.5"><rect x="6" y="4" width="18" height="26" rx="2"/><line x1="10" y1="12" x2="20" y2="12"/><line x1="10" y1="17" x2="20" y2="17"/><line x1="10" y1="22" x2="16" y2="22"/><circle cx="25" cy="24" r="5"/></svg></div>
    <h3>Proven process</h3>
    <p>We have carefully crafted each step in our process for successful outcomes.</p>
  </div>
  <div class="feature" style="left:827px;top:355px">
    <div class="icon"><svg width="34" height="34" viewBox="0 0 34 34" fill="none" stroke="#c07aa9" stroke-width="1.5"><circle cx="16" cy="18" r="11"/><circle cx="16" cy="18" r="6"/><circle cx="16" cy="18" r="1.5"/><path d="M16 18 28 6M24 6h4v4"/></svg></div>
    <h3>Exceeding your goals</h3>
    <p>We have carefully crafted each step in our process for successful outcomes.</p>
  </div>
  <div class="abs pink-disc"></div>
</section>

<section class="explore">
  <h2 class="section-title heading">Explore<span class="dot">.</span> Inspire<span class="dot">.</span> Engage<span class="dot">.</span></h2>
  <div class="tile" style="left:143px"><div class="photo" role="img" aria-label="Team reviewing printed advertising layouts on a table" style="background:linear-gradient(135deg,#c9c3b8,#e08a4f 60%,#3d5a80)"></div><span>Advertising</span></div>
  <div class="tile" style="left:377px"><div class="photo" role="img" aria-label="Business strategy meeting in a bright office" style="background:linear-gradient(135deg,#c89b5c,#4b3b30 60%,#2a2a35)"></div><span>Business Strategy</span></div>
  <div class="tile" style="left:610px"><div class="photo" role="img" aria-label="Design software open on a desktop monitor" style="background:linear-gradient(135deg,#e9e6e2,#9ca3ab 55%,#3b3b3b)"></div><span>Design</span></div>
  <div class="tile" style="left:844px"><div class="photo" role="img" aria-label="Marketing analytics dashboard on screens" style="background:linear-gradient(135deg,#dbe8f4,#5b8fc7 55%,#24406b)"></div><span>Marketing</span></div>
</section>

<section class="reviews">
  <h2 class="section-title heading">What Our <span style="color:#555">Client Says</span></h2>
  <div class="review" style="left:143px"><div class="stars">★★★★★</div><p>“ Brightwell Pixel provided us with a high quality, functional, easy to navigate and beautiful website ”</p><div class="person"><div class="avatar" role="img" aria-label="Client portrait"></div><div><b>RIVAS</b><small>USA</small></div></div></div>
  <div class="review" style="left:452px"><div class="stars">★★★★★</div><p>“ Brightwell Pixel provided us with a high quality, functional, easy to navigate and beautiful website ”</p><div class="person"><div class="avatar" role="img" aria-label="Client portrait"></div><div><b>RIVAS</b><small>USA</small></div></div></div>
  <div class="review" style="left:761px"><div class="stars">★★★★★</div><p>“ Brightwell Pixel provided us with a high quality, functional, easy to navigate and beautiful website ”</p><div class="person"><div class="avatar" role="img" aria-label="Client portrait"></div><div><b>RIVAS</b><small>USA</small></div></div></div>
</section>

<section class="partners">
  <h2 class="section-title heading">Our <span style="color:#555">Partners</span></h2>
  <div class="pager" style="left:80px"><svg width="8" height="10"><path d="M8 0 0 5 8 10z" fill="#333"/></svg></div>
  <div class="partner" style="left:150px"><i></i>LinkHarbor</div>
  <div class="partner" style="left:336px">northvale</div>
  <div class="partner" style="left:521px">Kettle &amp; Co</div>
  <div class="partner" style="left:707px">brightcart</div>
  <div class="partner" style="left:892px"><i></i>Keystep</div>
  <div class="pager" style="left:1090px"><svg width="8" height="10"><path d="M0 0 8 5 0 10z" fill="#333"/></svg></div>
</section>

<section class="contact">
  <div class="abs ring"></div>
  <h2 class="section-title heading"><span class="faint">Let’s Work</span> Together</h2>
  <div class="field" style="left:143px;top:152px">Name</div>
  <div class="field" style="left:454px;top:152px">Phone</div>
  <div class="field" style="left:765px;top:152px">Email</div>
  <div class="field select" style="left:143px;top:216px">I'm interested in</div>
  <div class="field" style="left:454px;top:216px">Business name</div>
  <div class="field" style="left:765px;top:216px">Website URL</div>
  <div class="field message" style="left:143px;top:281px">Message</div>
  <div class="btn" style="left:512px;top:417px;width:178px;height:45px">Submit Now <span class="arrow"></span></div>
</section>

<footer class="site-footer">
  <div class="abs logo" style="left:143px;top:96px;font-size:34px">brightwellpixel<span class="dot">.</span></div>
  <div class="social" style="left:197px"><i></i></div>
  <div class="social" style="left:245px"><i></i></div>
  <div class="social" style="left:292px"><i></i></div>
  <div class="divider" style="left:458px"></div>
  <div class="divider" style="left:727px"></div>
  <div class="col-title" style="left:538px">QUICK LINKS</div>
  <ul class="links"><li>Home</li><li>Our Services</li><li>Inspire</li><li>About</li><li>Collaborate</li><li>Connect</li></ul>
  <div class="col-title" style="left:810px">CONTACT INFO</div>
  <div class="info" style="top:96px"><svg width="16" height="20" viewBox="0 0 16 20"><path d="M8 1a6 6 0 0 0-6 6c0 5 6 12 6 12s6-7 6-12a6 6 0 0 0-6-6z" fill="none" stroke="#c07aa9" stroke-width="1.8"/><circle cx="8" cy="7" r="2" fill="#c07aa9"/></svg><span>48 Alder Lane. Portland, OR 97201,<br>USA</span></div>
  <div class="info" style="top:154px"><svg width="18" height="14" viewBox="0 0 18 14"><rect x="1" y="1" width="16" height="12" fill="#c07aa9"/><path d="M1 1l8 7 8-7" fill="none" stroke="#fff" stroke-width="1.4"/></svg><span>hello@brightwellpixel-example.com</span></div>
  <div class="info" style="top:193px"><svg width="18" height="18" viewBox="0 0 18 18"><path d="M4 1l3 4-2 2a10 10 0 0 0 6 6l2-2 4 3-2 3C8 17 1 10 1 3z" fill="#c07aa9"/></svg><span style="text-decoration:underline;font-weight:500">555-014-2270</span></div>
  <div class="copyright">© 2024 Brightwell Pixel, LLC. All Rights Reserved.</div>
  <div class="legal"><span>Privacy</span><span>|</span><span>Terms</span><span>|</span><span>Disclaimer</span></div>
</footer>

</body>
</html>
```